Creative Swimming Pool Facebook Design

We need A creative Facebook Page for a swimming pool company named "Wavecrest Pools" using our logo. Our slogan is "better service for a better price." the design should have a Connecticut feel to it (not tropics).

Industry/Entity Type

It Company

Font styles to use
Serif
Sans Serif

```html
<!DOCTYPE html>
<html lang="en">
<head>
<meta charset="utf-8">
<title>Wavecrest Pools – Cover</title>
<link href="https://fonts.googleapis.com/css2?family=Crimson+Text:ital,wght@0,600;1,400&display=swap" rel="stylesheet">
<style>
  :root {
    --page-bg: #e9eaed;
    --water-deep: #062a55;
    --water-mid: #0d5fa0;
    --water-light: #2f9fd6;
    --band-dark: #000a3a;
    --band-mid: #062a8a;
    --frame: #1f2630;
    --white: #ffffff;
    --brand-blue: #2a86c8;
  }
  html, body {
    margin: 0;
    padding: 0;
    width: 1200px;
    height: 1000px;
    overflow: hidden;
    background: var(--page-bg);
  }
  .canvas {
    position: relative;
    width: 1200px;
    height: 1000px;
  }
  .cover {
    position: absolute;
    left: 20px;
    top: 298px;
    width: 1158px;
    height: 428px;
    border: 1px solid var(--frame);
    overflow: hidden;
  }
  .cover-water {
    position: absolute;
    inset: 0;
    background:
      radial-gradient(ellipse 55% 60% at 55% 65%, var(--water-light) 0%, transparent 70%),
      radial-gradient(ellipse 70% 50% at 30% 30%, var(--water-mid) 0%, transparent 75%),
      linear-gradient(180deg, var(--water-deep) 0%, var(--water-mid) 55%, var(--water-deep) 100%);
  }
  .slogan-band {
    position: absolute;
    left: 0;
    right: 0;
    top: 182px;
    height: 64px;
    background: linear-gradient(90deg, var(--band-dark) 0%, var(--band-mid) 50%, var(--band-dark) 100%);
    display: flex;
    align-items: center;
    justify-content: center;
  }
  .slogan {
    margin: 0;
    font-family: "Crimson Text", Georgia, serif;
    font-style: italic;
    font-weight: 400;
    font-size: 37px;
    letter-spacing: 3px;
    color: var(--white);
    padding-bottom: 4px;
  }
  .profile-card {
    position: absolute;
    left: 43px;
    top: 558px;
    width: 224px;
    height: 224px;
    background: var(--white);
    border: 1px solid var(--frame);
    border-radius: 5px;
    display: flex;
    align-items: center;
    justify-content: center;
    gap: 8px;
  }
  .brand-dot {
    width: 12px;
    height: 12px;
    border-radius: 50%;
    background: var(--brand-blue);
    flex: none;
  }
  .brand-name {
    font-family: "Crimson Text", Georgia, serif;
    font-weight: 600;
    font-size: 25px;
    color: var(--brand-blue);
    white-space: nowrap;
  }
</style>
</head>
<body>
  <main class="canvas">
    <section class="cover">
      <div class="cover-water" role="img" aria-label="Photograph of rippling blue swimming pool water with light caustics"></div>
      <div class="slogan-band">
        <p class="slogan">better service for a better price</p>
      </div>
    </section>
    <div class="profile-card">
      <span class="brand-dot"></span>
      <span class="brand-name">Wavecrest Pools</span>
    </div>
  </main>
</body>
</html>
```